Detail Shop Business card design

i need a business card design for my new detailing company called 'Brenner's Detail Shop'. i want an all black and white design . simple, direct and to the point. i want the designer to choose a fitting font to match the logothe front should have logo, address, phone and email and the back side should have a slogan and text indicating that we offer services on anything including cars, trucks, motorcycles and RVs. slogan will read "we take pride in your ride"
maybe also very small on the back side the IG icon with Brenners_Detail_Shop

phone 482.615.7734
address 7384 E Harlow Ave
Spokane WA 99342
email: BrennersDetail@quorvail.com

Target Market(s)

all ages , auto enthusiasts

Industry/Entity Type

Automotive

Contact Information for Business Card

the front should have logo, address, phone and email and the back side should have a slogan and text indicating that we offer services on anything including cars, trucks, motorcycles and RVs. slogan will read "we take pride in your ride"

phone 482.615.7734
address 7384 E Harlow Ave
Spokane WA 99342

Colors
000000
ffffff

Requirements
Must have
• bold font and very simple design with good spacing
Nice to have
• anything creative from the designer indicating we service any types of vehicles
Should not have
• any colors ,

```html
<!DOCTYPE html>
<html lang="en">
<head>
<meta charset="utf-8">
<title>Brenner's Detail Shop – Business Card</title>
<link href="https://fonts.googleapis.com/css2?family=Roboto+Slab:wght@400;800&display=swap" rel="stylesheet">
<style>
  :root {
    --ink: #000000;
    --paper: #ffffff;
    --backdrop: #2b2c2e;
    --shade: #3a3a3a;
  }
  * { box-sizing: border-box; margin: 0; padding: 0; }
  html, body {
    width: 1200px; height: 900px; overflow: hidden;
    background: var(--backdrop);
    font-family: "Roboto Slab", Georgia, serif;
    color: var(--ink);
  }
  .stage {
    width: 1200px; height: 900px;
    display: flex; flex-direction: column;
    align-items: center; justify-content: center; gap: 40px;
  }
  .card {
    width: 700px; height: 400px;
    background: var(--paper);
    position: relative;
    overflow: hidden;
    box-shadow: 0 10px 30px rgba(0,0,0,.45);
  }

  /* Front: brand + slogan */
  .card--front {
    display: flex; align-items: center;
    padding: 0 56px 0 48px; gap: 40px;
  }
  .brand {
    width: 220px;
    display: flex; flex-direction: column; align-items: center; gap: 14px;
    text-align: center;
  }
  .brand__mark {
    width: 56px; height: 56px; border-radius: 50%;
    background: var(--ink);
  }
  .brand__name {
    font-weight: 800; font-size: 26px; line-height: 1.15;
    text-transform: uppercase; letter-spacing: .5px;
  }
  .pitch { flex: 1; }
  .slogan {
    font-weight: 800; font-size: 48px; line-height: .98;
    text-transform: uppercase; letter-spacing: -.5px;
  }
  .services {
    font-weight: 400; font-size: 19px; line-height: 1.3;
    margin-top: 12px;
  }

  /* Back: slogan + contact + vehicle art */
  .card--back { padding: 40px 44px; }
  .card--back .slogan { font-size: 40px; }
  .card--back .services { font-size: 15px; max-width: 330px; margin-top: 8px; }
  .contact {
    list-style: none; margin-top: 22px;
    font-size: 16px; line-height: 1.25;
    display: flex; flex-direction: column; gap: 9px;
  }
  .contact__item { display: flex; align-items: flex-start; gap: 12px; }
  .contact__icon { width: 16px; height: 16px; flex: none; margin-top: 2px; }
  .vehicle-art {
    position: absolute; right: 0; bottom: 0;
    width: 310px; height: 250px;
    background: linear-gradient(200deg, #5a5a5a 0%, #111 55%, #000 100%);
    border-top-left-radius: 140px 90px;
  }
</style>
</head>
<body>
<main class="stage">

  <section class="card card--front" aria-label="Card front">
    <div class="brand">
      <span class="brand__mark" aria-hidden="true"></span>
      <p class="brand__name">Brenner's Detail Shop</p>
    </div>
    <div class="pitch">
      <h1 class="slogan">We take pride<br>in your ride</h1>
      <p class="services">We offer services on anything including cars, trucks, motorcycles and RVs.</p>
    </div>
  </section>

  <section class="card card--back" aria-label="Card back">
    <h2 class="slogan">We take pride<br>in your ride</h2>
    <p class="services">We offer services on anything including cars, trucks, motorcycles and RVs.</p>
    <ul class="contact">
      <li class="contact__item">
        <svg class="contact__icon" viewBox="0 0 24 24" aria-hidden="true"><path fill="#000" d="M6.6 10.8a15.1 15.1 0 0 0 6.6 6.6l2.2-2.2a1 1 0 0 1 1-.25 11.4 11.4 0 0 0 3.6.57 1 1 0 0 1 1 1V20a1 1 0 0 1-1 1A17 17 0 0 1 3 4a1 1 0 0 1 1-1h3.5a1 1 0 0 1 1 1c0 1.25.2 2.45.57 3.57a1 1 0 0 1-.25 1z"/></svg>
        <span>482.615.7734</span>
      </li>
      <li class="contact__item">
        <svg class="contact__icon" viewBox="0 0 24 24" aria-hidden="true"><rect x="2" y="5" width="20" height="14" rx="1.5" fill="#000"/><path d="M3 6.5l9 6.5 9-6.5" fill="none" stroke="#fff" stroke-width="1.8"/></svg>
        <span>BrennersDetail@quorvail.com</span>
      </li>
      <li class="contact__item">
        <svg class="contact__icon" viewBox="0 0 24 24" aria-hidden="true"><circle cx="12" cy="12" r="9" fill="none" stroke="#000" stroke-width="2.4"/></svg>
        <span>Brenners_Detail_Shop</span>
      </li>
      <li class="contact__item">
        <svg class="contact__icon" viewBox="0 0 24 24" aria-hidden="true"><path fill="#000" d="M12 2a7 7 0 0 0-7 7c0 5.2 7 13 7 13s7-7.8 7-13a7 7 0 0 0-7-7zm0 9.5A2.5 2.5 0 1 1 12 6.5a2.5 2.5 0 0 1 0 5z"/></svg>
        <span>7384 E Harlow Ave<br>Spokane WA 99342</span>
      </li>
    </ul>
    <div class="vehicle-art" role="img" aria-label="Black and white illustration of a classic hot rod seen from the front corner"></div>
  </section>

</main>
</body>
</html>
```